Etiketten-Design für Weinflasche
Helga hat mit sehr viel Mühe und Hingabe unsere Wünsche umgesetzt. Wir sind mit dem Endergebnis sehr zufrieden.
Zielgruppe
Wir sind ein Weingut-Startup und suchen ein frisches, hochwertiges Design für unsere Flaschenetiketten.
Aufgabenstellung
Wir benötigen ein Vorderetikett für unsere Weinflaschen mit folgenden Vorgaben:
- Etiketten sollen variabel nutzbar sein, für verschiedene Rebsorten bspw. in versch. Farben
- Auf dem Etikett zwingend: Logo (siehe Anlage), Rebsorte, Anbaugebiet (Nahe)
- Wiedererkennungswert
- nicht zu klassisch, nicht zu futuristisch (gutes Mittelmaß, wie beim Logo auch)
- ggf. Spiel mit (Hintergrund-)Farben für verschiedene Sorten, ggf. Hintergrundmuster (evtl. Höhenlinien des Talwiesers, Bad Kreuznach (unser Heimatberg))
- Anpassung an verschiedene Qualitätsstufen (Gutswein, Ortswein, Lagenwein), ggf. schwarzes Sonderetikett für absolutes Premiumsegment
- unsere Werte als Naturnah und familiengeführtes Weingut sollen transportiert werden
- Maß: 80x90mm (breitxhoch)
Insgesamt sind wir offen für verschiedene Vorschläge, auch wenn die Vorgaben oben teils sehr konkret sind. Bei guten Designs lassen wir uns gerne von unseren Vorstellungen abbringen ;)

```html
<!DOCTYPE html>
<html lang="de">
<head>
<meta charset="utf-8">
<title>Lenzhof – Traubenwein Etikett</title>
<link rel="stylesheet" href="https://fonts.googleapis.com/css2?family=Oswald:wght@300;400&display=swap">
<style>
  :root {
    --backdrop: #e3e3e3;
    --paper: #ffffff;
    --frame-dark: #5c8a2a;
    --frame-light: #7cc04a;
    --ink: #5e7a2e;
    --contour: rgba(196, 208, 170, 0.55);
    --contour-soft: rgba(214, 222, 194, 0.45);
    --cluster: rgba(225, 228, 216, 0.75);
  }
  * { box-sizing: border-box; margin: 0; padding: 0; }
  html, body {
    width: 1200px; height: 1200px; overflow: hidden;
    background: var(--backdrop);
    font-family: "Oswald", sans-serif;
  }
  .label {
    position: absolute; left: 332px; top: 220px;
    width: 536px; height: 760px;
    background: var(--paper);
    box-shadow: -6px 8px 14px rgba(0,0,0,0.18);
    overflow: hidden;
  }
  .label__pattern {
    position: absolute; inset: 0;
    background:
      radial-gradient(ellipse 34% 50% at 50% 62%, var(--cluster) 0%, rgba(225,228,216,0) 100%),
      radial-gradient(ellipse 42% 48% at 100% 30%, var(--contour) 0%, rgba(196,208,170,0) 100%),
      radial-gradient(ellipse 36% 30% at 18% 48%, var(--contour) 0%, rgba(196,208,170,0) 100%),
      radial-gradient(ellipse 55% 40% at 25% 90%, var(--contour-soft) 0%, rgba(214,222,194,0) 100%),
      radial-gradient(ellipse 45% 35% at 80% 95%, var(--contour-soft) 0%, rgba(214,222,194,0) 100%);
  }
  .label__frame {
    position: absolute; left: 23px; top: 22px; right: 23px; bottom: 22px;
    border-radius: 22px;
    border: 12px solid var(--frame-dark);
  }
  .label__frame::before {
    content: ""; position: absolute; left: 30%; right: 30%; top: -12px; height: 12px;
    background: linear-gradient(90deg, var(--frame-dark), var(--frame-light), var(--frame-dark));
  }
  .brand {
    position: absolute; left: 0; right: 0; top: 70px;
    display: flex; justify-content: center; align-items: center; gap: 12px;
    color: var(--ink);
    font-weight: 300; font-size: 60px; line-height: 1.2;
  }
  .brand__dot {
    width: 14px; height: 14px; border-radius: 50%; background: var(--ink);
  }
  .variety {
    position: absolute; left: 0; right: 0; top: 258px;
    text-align: center; color: var(--ink); font-weight: 300;
  }
  .variety__top { font-size: 84px; line-height: 1; letter-spacing: -1px; }
  .variety__rule {
    width: 210px; height: 2px; background: var(--ink);
    margin: 16px auto 18px;
  }
  .variety__bottom {
    display: flex; justify-content: center; align-items: center; gap: 44px;
    font-size: 84px; line-height: 1;
  }
  .grape-icon {
    width: 18px; height: 34px; background: var(--ink);
    border-radius: 50% 50% 50% 50% / 35% 35% 65% 65%;
  }
  .volume {
    position: absolute; left: 0; right: 0; top: 538px;
    text-align: center; color: var(--ink);
    font-weight: 300; font-size: 32px;
  }
  .seal {
    position: absolute; left: 354px; top: 572px;
    width: 100px; height: 100px;
  }
  .seal svg { display: block; }
  .seal__text {
    position: absolute; inset: 0;
    display: flex; align-items: center; justify-content: center;
    color: #fff; font-size: 17px; font-weight: 300;
    transform: rotate(-8deg);
  }
</style>
</head>
<body>
  <article class="label">
    <div class="label__pattern" role="img" aria-label="Feine Höhenlinien des Heimatbergs mit blasser Traubensilhouette als Hintergrundmuster"></div>
    <div class="label__frame"></div>

    <header class="brand">
      <span class="brand__dot"></span>
      <span class="brand__name">Lenzhof</span>
    </header>

    <div class="variety">
      <div class="variety__top">TRAUBEN</div>
      <div class="variety__rule"></div>
      <div class="variety__bottom">
        <span class="grape-icon" role="img" aria-label="Kleine Traubenrebe"></span>
        <span>WEIN</span>
        <span class="grape-icon" role="img" aria-label="Kleine Traubenrebe"></span>
      </div>
    </div>

    <div class="volume">100ML</div>

    <div class="seal">
      <svg width="100" height="100" viewBox="0 0 98 98" aria-hidden="true">
        <defs>
          <radialGradient id="sealFill" cx="40%" cy="35%" r="70%">
            <stop offset="0%" stop-color="#7cc04a"/>
            <stop offset="100%" stop-color="#4f9028"/>
          </radialGradient>
        </defs>
        <polygon fill="#5aa02e" points="49,2 56,8 65,5 69,13 78,13 79,22 87,26 84,34 91,40 86,48 91,56 84,62 87,71 79,75 78,84 69,84 65,92 56,89 49,95 42,89 33,92 29,84 20,84 19,75 11,71 14,62 7,56 12,48 7,40 14,34 11,26 19,22 20,13 29,13 33,5 42,8"/>
        <circle cx="49" cy="49" r="36" fill="url(#sealFill)"/>
      </svg>
      <div class="seal__text">ORIGINAL</div>
    </div>
  </article>
</body>
</html>
```